Sharper Daily Habits Qorafone App

I am looking to create an Qorafone app (support Qorafone 5 and above) that will inspire and empower the app user to be more productive through a creative, interative and simplistic user experience that teaches the 10 topics related to "Sharper Daily Habits". Please see attached zip files for the 10 topic as PDF files and 20 posters (20 jpg files) which include a quote related to the content bundle’s topic.

Target Market(s)

working professionals who desire to be more productive in their ways of doing

Industry/Entity Type

It Support

Font styles to use
Sans Serif

Colors
33a6d7
0255a3
9bcb3b
cadf82
33b8a4

Requirements
Must have
• don't really wanna say "ebook" style app which would be below my expectation, i expect something more creative than an "ebook" app. i prefer you use your creativity to come up with the design but if you are a bit lost, please read below.
• some specs in my mind:
• - 10 flash cards design for each of the topic so they can be used in a carousel style menu (see sample app screenshot 1 - 1st screen to the left)
• - when presenting a topic, the background should be the same as the flash card of the topic (see sample app screenshot 2 - the right most screen)
• - at the bottom of the topic screen, a audio play/pause buttons bar should be presented as the app will play audible version for the article.
• - the fashion of the sample app screen shots shouldn't be followed as it is an ancient fashion reflecting the content. I expect the fashion of the app should be modern and reflect the topic "sharper daily habits"
• Screens required:
• - Main menu screen: carosoul style presenting the 10 topics using flash cards, should have a "play/pause" button to play the audible topic
• - Topic screen: presents the text content of the topic with flash card design as the background, paging buttons when content spans over one page, have media player bar at bottom to "play/pause/fast forward/reverse" audible
Nice to have
• i have 20 posters with quotes that inspires the user. i would like to see the posters to be presented full screen with a "inspire me" button somewhere which will randomly display a poster to the user.

```html
<!DOCTYPE html>
<html lang="en">
<head>
<meta charset="utf-8">
<title>Elevaro – Topic Screen</title>
<link href="https://fonts.googleapis.com/css2?family=Roboto:wght@300;400;500;700&display=swap" rel="stylesheet">
<style>
  :root {
    --page-bg: #f6f7f9;
    --brand-blue: #0b56a4;
    --accent-blue: #33a6d7;
    --control-blue: #1f5aa8;
    --control-soft: #5b7fc0;
    --ink: #111111;
    --ink-soft: #333333;
    --white: #ffffff;
    --photo-dark-1: #3a3a3a;
    --photo-dark-2: #262626;
    --player-1: #eef0f2;
    --player-2: #dcdfe3;
  }
  * { box-sizing: border-box; margin: 0; padding: 0; }
  html, body {
    width: 1200px; height: 1000px; overflow: hidden;
    background: var(--page-bg);
    font-family: "Roboto", Arial, sans-serif;
  }
  .screen {
    position: absolute; left: 387px; top: 124px;
    width: 422px; height: 747px;
    overflow: hidden; background: var(--white);
  }
  .status-bar {
    position: absolute; left: 0; top: 0; width: 100%; height: 24px;
    background: var(--brand-blue); color: var(--white);
    font-size: 12.5px; font-weight: 700;
  }
  .status-bar .signal { position: absolute; left: 10px; top: 6px; }
  .status-bar .clock { position: absolute; left: 0; right: 0; top: 5px; text-align: center; }
  .status-bar .battery { position: absolute; right: 8px; top: 5px; display: flex; align-items: center; gap: 3px; }
  .nav-bar {
    position: absolute; left: 0; top: 24px; width: 100%; height: 56px;
    background: var(--brand-blue); color: var(--white);
  }
  .nav-bar .back {
    position: absolute; left: 10px; top: 17px;
    display: flex; align-items: center; gap: 4px;
    font-size: 21px; font-weight: 300;
  }
  .nav-bar .app-name {
    position: absolute; left: 0; right: 0; top: 19px; text-align: center;
    font-size: 17.5px; font-weight: 700; letter-spacing: 0.3px;
  }
  .topic-card {
    position: absolute; left: 0; top: 80px; width: 100%; height: 518px;
    color: var(--white);
  }
  .topic-card .backdrop {
    position: absolute; inset: 0;
    background: radial-gradient(ellipse at 50% 55%, #4a4644 0%, var(--photo-dark-1) 45%, var(--photo-dark-2) 100%);
  }
  .topic-card .title {
    position: absolute; left: 0; right: 0; top: 16px; text-align: center;
    font-size: 17.5px; font-weight: 700; line-height: 23px;
  }
  .topic-card .divider {
    position: absolute; left: 142px; top: 81px; width: 137px; height: 1px;
    background: rgba(255,255,255,0.7);
  }
  .topic-card .article {
    position: absolute; left: 29px; top: 101px; width: 380px;
    font-size: 17px; font-weight: 300; line-height: 22.5px;
  }
  .topic-card .article h2 { font-size: 17.5px; font-weight: 700; line-height: 22.5px; }
  .topic-card .tip-button { position: absolute; left: 192px; top: 432px; }
  .topic-card .pager {
    position: absolute; left: 0; right: 0; top: 492px;
    display: flex; justify-content: center; align-items: center; gap: 5px;
  }
  .pager .dot { width: 8px; height: 8px; border-radius: 50%; background: var(--white); }
  .pager .dot.active { width: 10px; height: 10px; }
  .player {
    position: absolute; left: 0; top: 598px; width: 100%; height: 149px;
    background: linear-gradient(180deg, var(--player-1) 0%, var(--player-2) 60%, #e6e8eb 100%);
    color: var(--ink);
  }
  .player .progress-track { position: absolute; left: 0; top: 0; width: 100%; height: 2px; background: #c9ccd0; }
  .player .progress-fill { position: absolute; left: 0; top: 0; width: 279px; height: 3px; background: var(--accent-blue); }
  .player .progress-head { position: absolute; left: 278px; top: 0; width: 2px; height: 18px; background: var(--accent-blue); }
  .player .time { position: absolute; top: 17px; font-size: 12.5px; color: var(--ink-soft); }
  .player .time.elapsed { left: 15px; }
  .player .time.remaining { right: 17px; }
  .player .track-title {
    position: absolute; left: 0; right: 0; top: 29px; text-align: center;
    font-size: 17.5px; font-weight: 700;
  }
  .player .controls { position: absolute; left: 0; top: 66px; width: 100%; height: 28px; }
  .player .volume { position: absolute; left: 38px; top: 108px; width: 348px; height: 24px; }
</style>
</head>
<body>
  <main class="screen">
    <div class="status-bar">
      <svg class="signal" width="56" height="12" viewBox="0 0 56 12" aria-hidden="true">
        <g fill="#fff"><circle cx="3" cy="6" r="3"/><circle cx="10" cy="6" r="3"/><circle cx="17" cy="6" r="3"/><circle cx="24" cy="6" r="3"/><circle cx="31" cy="6" r="3"/></g>
        <g fill="none" stroke="#fff" stroke-width="1.6" stroke-linecap="round">
          <path d="M38 4.5 a9 9 0 0 1 12 0"/><path d="M40.5 7 a5.5 5.5 0 0 1 7 0"/>
        </g>
        <circle cx="44" cy="10" r="1.3" fill="#fff"/>
      </svg>
      <div class="clock">9:41 AM</div>
      <div class="battery">
        <span>100%</span>
        <svg width="27" height="12" viewBox="0 0 27 12" aria-hidden="true">
          <rect x="0.75" y="0.75" width="22.5" height="10.5" rx="2" fill="none" stroke="#fff" stroke-width="1.3"/>
          <rect x="2.5" y="2.5" width="19" height="7" rx="1" fill="#fff"/>
          <rect x="24.5" y="4" width="2" height="4" rx="0.8" fill="#fff"/>
        </svg>
      </div>
    </div>

    <header class="nav-bar">
      <div class="back">
        <svg width="13" height="22" viewBox="0 0 13 22" aria-hidden="true"><path d="M11 2 L2 11 L11 20" fill="none" stroke="#fff" stroke-width="2.4" stroke-linecap="round" stroke-linejoin="round"/></svg>
        <span>Back</span>
      </div>
      <div class="app-name">ELEVARO</div>
    </header>

    <section class="topic-card">
      <div class="backdrop" role="img" aria-label="Dimmed blurred topic photo of a person standing on a beach at dusk"></div>
      <h1 class="title">An Introduction to Highly Productive<br>Flow States</h1>
      <div class="divider"></div>
      <article class="article">
        <h2>What is Flow?</h2>
        <p>Most of us will have experienced flow at one<br>time or other in our lives. Most people descr-<br>ibe flow as being that point when you're surf-<br>ing, skiing or playing sports when everything<br>slows down and you are able to react with<br>super-human reactions. It's that sense of ca-<br>lm that allows you to pull off the impossible<br>and achieve amazing feats and it's thus highly<br>sought after by athletes.</p>
        <p>Flow is also that point in time when you're<br>writing and you completely focus on what yo-<br>u're doing to the extent that you don't even<br>get up to go to the toilet or eat.</p>
      </article>
      <svg class="tip-button" width="40" height="40" viewBox="0 0 40 40" role="img" aria-label="Tip">
        <circle cx="20" cy="20" r="18.5" fill="none" stroke="#fff" stroke-width="1.6"/>
        <path d="M20 11 a6.5 6.5 0 0 0 -4 11.6 v2.4 h8 v-2.4 A6.5 6.5 0 0 0 20 11z" fill="#fff"/>
        <rect x="16.5" y="26.3" width="7" height="1.6" rx="0.8" fill="#fff"/>
        <rect x="17.5" y="28.8" width="5" height="1.6" rx="0.8" fill="#fff"/>
      </svg>
      <div class="pager">
        <span class="dot"></span><span class="dot active"></span><span class="dot"></span><span class="dot"></span><span class="dot"></span>
      </div>
    </section>

    <section class="player">
      <div class="progress-track"></div>
      <div class="progress-fill"></div>
      <div class="progress-head"></div>
      <span class="time elapsed">5:00</span>
      <span class="time remaining">-1:10</span>
      <div class="track-title">Flow States</div>
      <svg class="controls" viewBox="0 0 422 28" aria-label="Playback controls" role="img">
        <g fill="var(--control-soft)">
          <path d="M126 5 L113 14 L126 23Z"/><path d="M140 5 L127 14 L140 23Z"/>
          <path d="M282 5 L295 14 L282 23Z"/><path d="M296 5 L309 14 L296 23Z"/>
        </g>
        <path d="M201 1 L227 14 L201 27Z" fill="var(--control-blue)"/>
      </svg>
      <svg class="volume" viewBox="0 0 348 24" aria-label="Volume" role="img">
        <path d="M2 9 h3 l4 -4 v14 l-4 -4 h-3z" fill="var(--control-soft)"/>
        <line x1="30" y1="12" x2="267" y2="12" stroke="var(--control-blue)" stroke-width="1.5"/>
        <line x1="267" y1="12" x2="312" y2="12" stroke="#b5b9bf" stroke-width="1.5"/>
        <circle cx="267" cy="12" r="8.5" fill="#fff" stroke="#c9ccd0" stroke-width="0.8"/>
        <path d="M327 9 h3 l4 -4 v14 l-4 -4 h-3z" fill="var(--control-soft)"/>
        <path d="M337 9 a4 4 0 0 1 0 6 M340 6.5 a7.5 7.5 0 0 1 0 11" fill="none" stroke="var(--control-soft)" stroke-width="1.4" stroke-linecap="round"/>
      </svg>
    </section>
  </main>
</body>
</html>
```